Einladung zum Geburtstag
Einladung zu einer Geburtstagsparty von zwei "Mädels", die zusammen 99 Jahre jung werden.
Eine wird 55 (25.8.) die andere 44. (24.8.) - alles "Schnapszahlen".
Es soll eine kleine Party tagsüber für die Arbeitskollegen werden, mit Imbiss und Umtrunk. Termin für die Feier ist der 25.8. ab 14h.
Die Einladung soll sowohl gedruckt als auch per Mail verschickt werden können.

```html
<!DOCTYPE html>
<html lang="de">
<head>
<meta charset="utf-8">
<title>Einladung – Geburtstagsfeier</title>
<link rel="stylesheet" href="https://fonts.googleapis.com/css2?family=Poiret+One&display=swap">
<style>
  :root {
    --berry: #b0125a;
    --sun: #ffd21a;
    --amber: #f0a000;
    --glow: #fff4c8;
    --paper: #ffffff;
  }
  * { margin: 0; padding: 0; box-sizing: border-box; }
  html, body { width: 678px; height: 1200px; overflow: hidden; background: var(--paper); }
  body { font-family: "Poiret One", sans-serif; color: var(--paper); }

  .invitation { position: relative; width: 678px; height: 1200px; overflow: hidden; }

  .balloon-field {
    position: absolute; inset: 0 0 48px 0; z-index: 0;
    background:
      radial-gradient(ellipse at 30% 25%, var(--glow) 0%, var(--sun) 30%, var(--amber) 75%, #e48a00 100%);
  }

  .title-band {
    position: absolute; left: 0; top: 364px; width: 678px; height: 176px; z-index: 2;
    background: var(--berry);
    display: flex; align-items: center; justify-content: center;
  }
  .title { font-size: 146px; font-weight: 400; letter-spacing: 2px; line-height: 1; margin-top: -10px; white-space: nowrap; }

  .tagline {
    position: absolute; left: 60px; z-index: 3;
    background: var(--berry);
    font-size: 46px; line-height: 1; padding: 8px 12px 10px 12px;
    letter-spacing: 0.5px; white-space: nowrap;
    width: fit-content;
  }
  .tagline--first { top: 642px; }
  .tagline--second { top: 714px; }

  .age-flourish {
    position: absolute; left: 390px; top: 690px; width: 276px; height: 460px; z-index: 1;
    border-radius: 138px 138px 40px 138px;
    background: linear-gradient(160deg, rgba(176,18,90,0.55), rgba(176,18,90,0.95));
  }

  .date-band {
    position: absolute; left: 0; bottom: 0; width: 678px; height: 48px; z-index: 2;
    background: var(--berry);
    display: flex; align-items: baseline; padding: 6px 0 0 24px;
    font-size: 22px; gap: 14px; white-space: nowrap;
  }
  .date-band .big { font-size: 34px; }
  .date-band sup { font-size: 16px; text-decoration: underline; }
</style>
</head>
<body>
  <main class="invitation">
    <div class="balloon-field" role="img" aria-label="Muster aus gelb-orangen Luftballon-Kreisen"></div>

    <header class="title-band">
      <h1 class="title">Einladung</h1>
    </header>

    <div class="age-flourish" role="img" aria-label="Geschwungene Zahl 99 in Beerenrot"></div>

    <p class="tagline tagline--first">...Luftballons fliegen</p>
    <p class="tagline tagline--second">da am Horizont</p>

    <footer class="date-band">
      <span>am</span>
      <span class="big">25.08.2011</span>
      <span>ab</span>
      <span class="big">14<sup>00</sup></span>
      <span>Uhr</span>
    </footer>
  </main>
</body>
</html>
```